Collagen Tub Packaging Design for a New Brand

PLEASE DON'T SEND ANY NEW DESIGNS WE JUST HAVE TO DECIDE WITH MY PARTNERS THANKS A LOT.
I've created a very detailed document & design examples of what we like in certain designs and what we don't.

There are 3 documents:
1- Brief for the Design (please read it before designing)
2- Brand Design Examples that we like (and why we like them)
3- Die cut for the packaging design. This will be it's dimensions.

We are NOT looking for someone to micro-manage. In contrast, we want someone to help us express our ideas better with their design. Nothing I say in these briefs are there to limit the creativity of the designer, because if we knew exactly what we wanted we would do it ourselves but we trust the designer's expertise in this packaging design.

In short: We want our brand to feel premium, high-quality & trust worthy with it's design not feeling very busy or bloated. We don't have a logo source file, but you'll get the idea of what we want when you see it).

Let me know if you have any further questions, will answer each question real fast.

Thanks.

Target Market(s)

Pretty much everyone above 25+ in Turkey because nearly all of them are using are collagens so our audience is wild.

Industry/Entity Type

Collagen - Health, Wellness & Supplements

Font styles to use
Serif
Sans Serif

Colors

Designer to choose colors to be used in the design.

Requirements
Must have
• Our design should be distinct, a design style which everyone can identify from 10 meters away if they know the product. This is a MUST have for us. It's up to designer to achieve it. This can be just a simple color palette aswell.
Should not have
• It shouldn't feel bloated and very busy. Please avoid very detailed icons (as a rule of thumb, if you can make it work great)

```html
<!DOCTYPE html>
<html lang="en">
<head>
<meta charset="utf-8">
<title>Corvela Hydrolyzed Collagen Peptides – Label</title>
<link rel="stylesheet" href="https://fonts.googleapis.com/css2?family=Cinzel:wght@400;700&family=Raleway:wght@400;500&display=swap">
<style>
  :root {
    --bg: #bcd2fd;
    --label-white: #ffffff;
    --label-shade: #e4e4e6;
    --band-grey: #b4b5ba;
    --navy: #2a3388;
    --navy-deep: #232c7e;
    --navy-light: #5663ab;
    --text-grey: #7d828a;
    --soft-grey: #a7abb1;
    --silver: #c9cbd0;
    --on-navy: #dfe3f5;
  }
  html, body {
    margin: 0;
    padding: 0;
    width: 1200px;
    height: 1072px;
    overflow: hidden;
    background: var(--bg);
  }
  .canvas {
    position: relative;
    width: 1200px;
    height: 1072px;
  }
  .label {
    position: absolute;
    left: 320px;
    top: 266px;
    width: 560px;
    height: 540px;
  }
  .serif { font-family: "Cinzel", Georgia, serif; }
  .sans { font-family: "Raleway", Arial, sans-serif; }
  .brand-name { font-size: 24px; font-weight: 400; fill: var(--text-grey); letter-spacing: 0.5px; }
  .title-small { font-size: 25px; font-weight: 400; fill: var(--text-grey); }
  .title-main { font-size: 62px; font-weight: 700; fill: var(--navy); }
  .claim { font-size: 16px; fill: var(--soft-grey); font-weight: 400; }
  .support-area { font-size: 9.5px; fill: var(--text-grey); font-weight: 500; }
  .support-word { font-size: 13px; fill: #ffffff; font-weight: 500; letter-spacing: 0.3px; }
  .feature-text { font-size: 11.5px; fill: var(--on-navy); font-weight: 400; }
  .feature-mark { font-size: 8.5px; fill: var(--on-navy); font-weight: 400; }
  .flavor-text { font-size: 12.5px; fill: var(--on-navy); font-weight: 400; }
  .nutrient-value { font-size: 19px; fill: var(--on-navy); font-weight: 400; }
  .nutrient-unit { font-size: 14px; }
  .nutrient-name { font-size: 11px; fill: var(--on-navy); font-weight: 400; }
</style>
</head>
<body>
<div class="canvas">
  <svg class="label" viewBox="0 0 560 540" xmlns="http://www.w3.org/2000/svg">
    <defs>
      <linearGradient id="labelSurface" x1="0" y1="0" x2="1" y2="0">
        <stop offset="0" stop-color="var(--label-white)"/>
        <stop offset="0.45" stop-color="var(--label-white)"/>
        <stop offset="1" stop-color="var(--label-shade)"/>
      </linearGradient>
      <linearGradient id="navySurface" x1="0" y1="0" x2="1" y2="0">
        <stop offset="0" stop-color="var(--navy)"/>
        <stop offset="0.22" stop-color="var(--navy-light)"/>
        <stop offset="0.5" stop-color="var(--navy)"/>
        <stop offset="1" stop-color="var(--navy-deep)"/>
      </linearGradient>
      <linearGradient id="artTones" x1="0" y1="0" x2="1" y2="0">
        <stop offset="0" stop-color="#f3ecdf"/>
        <stop offset="0.35" stop-color="#e6eef6"/>
        <stop offset="0.7" stop-color="#e3f2f1"/>
        <stop offset="1" stop-color="#f1e9dc"/>
      </linearGradient>
      <clipPath id="labelClip">
        <rect x="0" y="0" width="560" height="540" rx="14"/>
      </clipPath>
    </defs>

    <g clip-path="url(#labelClip)">
      <rect class="label-body" x="0" y="0" width="560" height="540" fill="url(#labelSurface)"/>
      <rect class="top-band" x="0" y="0" width="560" height="20" fill="var(--band-grey)"/>

      <text class="brand-name sans" x="280" y="50" text-anchor="middle">Corvela</text>

      <text class="title-small serif" x="280" y="88" text-anchor="middle">HYDROLYZED</text>
      <text class="title-main serif" x="282" y="150" text-anchor="middle" textLength="338" lengthAdjust="spacingAndGlyphs">COLLAGEN</text>
      <text class="title-small serif" x="451" y="179" text-anchor="end">PEPTIDES</text>

      <rect class="hero-illustration" x="0" y="190" width="560" height="104" fill="url(#artTones)" opacity="0.7"
            role="img" aria-label="Line illustration of two reaching hands around a drop with a plus sign, crossed by teal, amber and navy collagen helix strands"/>

      <text class="claim sans" x="24" y="340">High-Quality</text>
      <text class="claim sans" x="546" y="338" text-anchor="end">High Absorption</text>

      <path class="base-panel" d="M0 350 H127 L281 417 L434 350 H560 V540 H0 Z" fill="url(#navySurface)"/>
      <path class="base-edge" d="M0 350 H127 L281 417 L434 350 H560" fill="none" stroke="var(--silver)" stroke-width="1.6"/>

      <g class="supports-cross">
        <rect x="267.5" y="300" width="27" height="100" rx="13.5" fill="var(--navy)" stroke="var(--silver)" stroke-width="1.2"/>
        <rect x="232" y="335.5" width="98" height="29" rx="14.5" fill="var(--navy)" stroke="var(--silver)" stroke-width="1.2"/>
        <rect x="268.6" y="336.6" width="24.8" height="26.8" fill="var(--navy)"/>
        <text class="support-word sans" x="281" y="354.5" text-anchor="middle">SUPPORTS</text>
        <text class="support-area sans" x="245" y="327" text-anchor="middle">SKIN</text>
        <text class="support-area sans" x="314" y="327" text-anchor="middle">HAIR</text>
        <text class="support-area sans" x="246" y="381" text-anchor="middle">NAILS</text>
        <text class="support-area sans" x="316" y="381" text-anchor="middle">JOINTS</text>
      </g>

      <g class="feature silicium">
        <path d="M452 375 h10 v6 h6 v10 h-6 v6 h-10 v-6 h-6 v-10 h6 z" fill="none" stroke="var(--on-navy)" stroke-width="1" stroke-linejoin="round"/>
        <text class="feature-mark sans" x="457" y="389" text-anchor="middle">Si+</text>
        <text class="feature-text sans" x="466" y="401">Silicium Plus</text>
      </g>
      <g class="feature vitamin-c">
        <path d="M452 417 h10 v6 h6 v10 h-6 v6 h-10 v-6 h-6 v-10 h6 z" fill="none" stroke="var(--on-navy)" stroke-width="1" stroke-linejoin="round"/>
        <text class="feature-mark sans" x="457" y="431" text-anchor="middle">C+</text>
        <text class="feature-text sans" x="466" y="442">Vitamin C Plus</text>
      </g>

      <rect class="flavor-pill" x="229" y="440" width="104" height="22" rx="11" fill="none" stroke="var(--silver)" stroke-width="1.4"/>
      <text class="flavor-text sans" x="281" y="455.5" text-anchor="middle">UNFLAVORED</text>

      <g class="nutrition sans">
        <text class="nutrient-value" x="182" y="500" text-anchor="middle">0<tspan class="nutrient-unit">g</tspan></text>
        <text class="nutrient-name" x="182" y="518" text-anchor="middle">Carbs</text>
        <text class="nutrient-value" x="229" y="500" text-anchor="middle">0<tspan class="nutrient-unit">g</tspan></text>
        <text class="nutrient-name" x="229" y="518" text-anchor="middle">Fat</text>
        <text class="nutrient-value" x="275" y="500" text-anchor="middle">0<tspan class="nutrient-unit">g</tspan></text>
        <text class="nutrient-name" x="275" y="518" text-anchor="middle">Sugar</text>
        <text class="nutrient-value" x="324" y="500" text-anchor="middle">11<tspan class="nutrient-unit">g</tspan></text>
        <text class="nutrient-name" x="324" y="518" text-anchor="middle">Protein</text>
        <text class="nutrient-value" x="377" y="500" text-anchor="middle">12<tspan class="nutrient-unit">g</tspan></text>
        <text class="nutrient-name" x="377" y="518" text-anchor="middle">Collagen</text>
      </g>
    </g>
  </svg>
</div>
</body>
</html>
```